Business Card Design Project

Build kick ass business card.
Updates

I just uploaded the Vorintex Logo in AI format, for those that were asking. It's looking real good and we'll be reviewing the designs soon. Thanks. 

Target Market(s)

Businesses in many verticals. Focusing on information security.

Vorintex, LLC
Gordon Bexley
Principal Security Consultant
Mobile: +1-602-555-0187
Email: Gordon.Bexley@Vorintex.example
Web: www.vorintex.example

Industry/Entity Type

Business

Requirements
Must have
• Design must look high-end, hi-tech stylish and minimalist

Be different – one that stands out from thousands of others

Does not have to be traditional rectangle

Would like logo integrated

```html
<!DOCTYPE html>
<html lang="en">
<head>
<meta charset="utf-8">
<title>Vorintex Business Card</title>
<link rel="stylesheet" href="https://fonts.googleapis.com/css2?family=PT+Sans:wght@400;700&family=Montserrat:wght@400&display=swap">
<style>
  :root {
    --backdrop: #000000;
    --card-white: #ffffff;
    --teal-light: #21799a;
    --teal-mid: #1f6482;
    --teal-dark: #1a4558;
    --brand-grey: #4a4a4a;
    --brand-dot: #2f9fd6;
    --text-light: #ffffff;
  }
  * { margin: 0; padding: 0; box-sizing: border-box; }
  html, body {
    width: 1200px;
    height: 900px;
    overflow: hidden;
    background: var(--backdrop);
  }
  .canvas {
    position: relative;
    width: 1200px;
    height: 900px;
    background: var(--backdrop);
  }
  .card {
    position: absolute;
    left: 103px;
    top: 154px;
    width: 985px;
    height: 559px;
    border-radius: 19px;
    overflow: hidden;
    background: var(--card-white);
  }
  .card-band {
    position: absolute;
    inset: 0;
    width: 100%;
    height: 100%;
  }
  .brand {
    position: absolute;
    left: 135px;
    top: 122px;
    display: flex;
    align-items: center;
    gap: 22px;
  }
  .brand-dot {
    width: 62px;
    height: 62px;
    border-radius: 50%;
    background: var(--brand-dot);
  }
  .brand-name {
    font-family: "Montserrat", sans-serif;
    font-weight: 400;
    font-size: 50px;
    letter-spacing: 2px;
    color: var(--brand-grey);
    line-height: 1;
  }
  .holder {
    position: absolute;
    left: 707px;
    top: 72px;
    color: var(--text-light);
    font-family: "PT Sans", sans-serif;
    font-variant: small-caps;
  }
  .holder-name {
    font-size: 28px;
    font-weight: 700;
    letter-spacing: 2px;
    line-height: 1.1;
  }
  .holder-title {
    font-size: 12px;
    font-weight: 700;
    letter-spacing: 1px;
    margin-top: 2px;
  }
  .contact {
    position: absolute;
    left: 611px;
    top: 394px;
    color: var(--text-light);
    font-family: "PT Sans", sans-serif;
    font-variant: small-caps;
    font-size: 22px;
    letter-spacing: 1.5px;
    line-height: 28px;
    list-style: none;
  }
  .contact-small { font-size: 17px; }
</style>
</head>
<body>
<main class="canvas">
  <section class="card" aria-label="Vorintex business card">
    <svg class="card-band" viewBox="0 0 985 559" preserveAspectRatio="none" aria-hidden="true">
      <defs>
        <linearGradient id="bandGradient" x1="1" y1="0" x2="0.2" y2="1">
          <stop offset="0" stop-color="var(--teal-light)"/>
          <stop offset="0.5" stop-color="var(--teal-mid)"/>
          <stop offset="1" stop-color="var(--teal-dark)"/>
        </linearGradient>
      </defs>
      <path d="M628 0 C 700 160, 520 360, 47 559 L 985 559 L 985 0 Z" fill="url(#bandGradient)"/>
    </svg>

    <div class="brand">
      <span class="brand-dot" aria-hidden="true"></span>
      <span class="brand-name">VORINTEX</span>
    </div>

    <div class="holder">
      <p class="holder-name">Gordon Bexley</p>
      <p class="holder-title">Principal Security Consultant</p>
    </div>

    <ul class="contact">
      <li>Vorintex, LLC</li>
      <li>Mobile: +1-602-555-0187</li>
      <li>Email: <span class="contact-small">Gordon.Bexley@Vorintex.example</span></li>
      <li>Web: <span class="contact-small">www.vorintex.example</span></li>
    </ul>
  </section>
</main>
</body>
</html>
```